Rioja winery needs a new label design

A family-owned winery in Spain's Rioja Oriental region is looking to create a new label for a wine named "Zunad" Arabic for Castle, that reflects the land from which the wine is born. From the remote village of Quel, La Rioja Oriental, with the backdrop of the Sierra Yerga mountains and the Barrio de Bodegas, or group of caves where locals have produced wines for centuries. Wine name:
2018 Zunad Rioja Tempranillo
Quel, Rioja Oriental
Spain

Font styles to use
Serif
Sans Serif
Decorative
Script

Requirements
Must have
• vines, vineyards, grapes
Nice to have
• mountains,
Should not have
• castles. we already have a label design with the castle

```html
<!DOCTYPE html>
<html lang="en">
<head>
<meta charset="utf-8">
<title>Zunad Rioja Tempranillo – Wine Label</title>
<link rel="stylesheet" href="https://fonts.googleapis.com/css2?family=Tinos&family=Kurale&display=swap">
<style>
  :root {
    --canvas-bg: #d9d6d3;
    --label-paper: #f3f1ee;
    --label-frame: #6b6866;
    --ink: #2b2a29;
    --accent-red: #b3232b;
    --landscape-dark: #4a4a48;
    --landscape-mid: #8d8c88;
    --landscape-light: #dedcd8;
  }
  * { box-sizing: border-box; margin: 0; padding: 0; }
  html, body {
    width: 1200px;
    height: 800px;
    overflow: hidden;
    background: var(--canvas-bg);
  }
  .canvas {
    position: relative;
    width: 1200px;
    height: 800px;
    display: flex;
    align-items: center;
    justify-content: center;
  }
  .label {
    position: relative;
    width: 440px;
    height: 640px;
    background: var(--label-paper);
    box-shadow: 0 2px 10px rgba(0,0,0,0.12);
    color: var(--ink);
    text-align: center;
  }
  .label-frame {
    position: absolute;
    inset: 12px;
    border: 1.5px solid var(--label-frame);
  }
  .origin {
    position: absolute;
    top: 42px;
    left: 0;
    right: 0;
    font-family: "Tinos", serif;
    font-size: 27px;
    letter-spacing: 0.5px;
  }
  .landscape {
    position: absolute;
    top: 100px;
    left: 50px;
    width: 340px;
    height: 250px;
    border-radius: 18px 18px 60px 60px / 18px 18px 40px 40px;
    background:
      linear-gradient(180deg,
        var(--landscape-light) 0%,
        var(--landscape-mid) 22%,
        var(--landscape-dark) 45%,
        var(--landscape-mid) 70%,
        var(--landscape-light) 100%);
  }
  .wine-name {
    position: absolute;
    top: 384px;
    left: 0;
    right: 0;
    font-family: "Kurale", serif;
    font-size: 32px;
    color: var(--ink);
  }
  .wine-style {
    position: absolute;
    top: 432px;
    left: 0;
    right: 0;
    font-family: "Tinos", serif;
    font-size: 19px;
    letter-spacing: 3px;
    color: var(--accent-red);
  }
  .vintage {
    position: absolute;
    top: 510px;
    left: 0;
    right: 0;
    font-family: "Tinos", serif;
    font-size: 25px;
  }
  .country {
    position: absolute;
    top: 548px;
    left: 0;
    right: 0;
    font-family: "Tinos", serif;
    font-size: 30px;
  }
</style>
</head>
<body>
  <main class="canvas">
    <section class="label">
      <div class="label-frame"></div>
      <p class="origin">QUEL, RIOJA ORIENTAL</p>
      <div class="landscape" role="img" aria-label="Engraved black and white landscape of terraced vineyards below the Sierra Yerga mountains"></div>
      <h1 class="wine-name">Zunad Rioja Tempranillo</h1>
      <p class="wine-style">BORDEAUX</p>
      <p class="vintage">2018</p>
      <p class="country">Spain</p>
    </section>
  </main>
</body>
</html>
```